Flyer-Design für Seniorenbetreuung
Zielgruppe
Wir sind eine Genossenschaft, welche ihren Immobilienbestand gern erweitern möchte. Dafür soll für unsere Partnerfirma (welche im Seniorenbetreuungssektor tätig ist) eine Flyer erdacht werden, welcher Senioren bzw. ihre Angehörigen anspricht die Wohneigentum besitzen. Viele Senioren besitzen Ein-, Mehrfamilienhäuser oder Eigentumswohnungen und können oder wollen diese nicht weiter vererben. Zusätzlich sind sie durch die Kosten des Eigentums, wie Steuern oder Instandhaltungskosten belastet. Unsere Genossenschaft bietet eine Lösung des Problems. Eine Übernahme des Eigentums bei gleichzeitigem lebenslangem Wohnrecht. Die Zielgruppe soll in dem Flyer auf die bestehende Probleme angesprochen werden und gleichzeitig eine individuelle Lösung angeboten werden, welche eine Mitgliedschaft in dem sozialen Verbund der Genossenschaft ist.
Aufgabenstellung
Der Designer hat hier völlig freie Hand. Es sollte auf die Zielgruppe passen.
Passende Texte soll sich der Designer selbst erdenken.
Nachtrag: Ich habe mittlerweile viele Zuschriften bekommen, dass die Aufgabenstellung sich Texte auszudenken etwas zu allgemein gefasst ist, daher versuche ich hier nochmal etwas Licht in Dunkle zu bringen. Ich habe genauso wenig eine Idee, wie und mit welcher Wortwahl ein Senior auf einfühlsame Weise darauf angesprochen werden soll, ob er nicht sein Haus verkaufen möchte. Meine bisherigen Ideen waren:
'Haben sie schon einmal über den Verkauf ihrer Immobilie nachgedacht? Wussten sie, dass sie ihr Wohneigentum im vollen Umfang weiter nutzen können, ohne weiter die Kosten tragen zu müssen? Sie wollen wissen wie? Rufen sie doch einfach an und ich werde ihnen genau erklären, welche Vorzüge die Mitgliedschaft in einer Genossenschaft mit sich bringt.'
Allerdings erscheint mir das viel zu direkt und ich finde nicht die richtigen Worte diese Personengruppe in dem Maße anzusprechen, wie es nötig wäre, um sie zu einem Anruf zu bewegen. Daher hatte ich gehofft, dass sie hier ein findiger Designer findet, welcher eine bessere kreative Art hat als ich.
Vielleicht ist es die falsche Plattform, vielleicht schaffen wir es nicht die Vorgaben zu spezifizieren. Bilder anzuordnen ist sicher sehr wichtig, auch ist es wichtig aufhellende Elemente einzubringen. Aber wir suchen jemanden der einen Flyer so gestalten kann das der Flyer etwas ausdrückt, das eine Botschaft vermittelt wird, das auf einem Blick der Senior den Wunsch verspürt, bei uns anzurufen. Das heißt viel wichtiger als Bilder, ist der Inhalt der Ansprache. Nicht unbedingt der Inhalt, sondern das WIE. Nochmal: wir wollen ältere Menschen dazu bewegen ihr Eigentum auf Grund von Reperaturrückstau, Überlastung, gesundheitlichen Einschränkungen, finanziellen Schwierigkeiten, zu großem Aufwand in eine Genossenschaft einzubringen. Ds heißt S..

```html
<!DOCTYPE html>
<html lang="de">
<head>
<meta charset="utf-8">
<title>Flyer – XY-Genossenschaft</title>
<link rel="stylesheet" href="https://fonts.googleapis.com/css2?family=Source+Sans+3:wght@400;600;700&family=PT+Serif&display=swap">
<style>
  :root {
    --navy: #283583;
    --green: #3f9b36;
    --white: #ffffff;
    --backdrop: #e8e3dc;
    --garden-sky: #8fb8d8;
    --garden-green: #5c8a3c;
    --garden-deep: #3d5f2a;
    --rose-green: #6f8f3e;
    --room-mauve: #8a6e7e;
    --room-light: #dcdde0;
  }
  * { margin: 0; padding: 0; box-sizing: border-box; }
  html, body { width: 1061px; height: 1200px; overflow: hidden; }
  body {
    background: var(--backdrop);
    position: relative;
    font-family: "Source Sans 3", "PT Sans", sans-serif;
  }
  .panel {
    position: absolute;
    top: 38px;
    width: 405px;
    height: 1143px;
    background: var(--white);
    overflow: hidden;
  }
  .panel--intro { left: 102px; }
  .panel--voices { left: 560px; }

  /* Intro panel */
  .intro-headline {
    position: absolute;
    left: 39px; top: 32px; width: 340px;
    color: var(--navy);
    font-weight: 700;
    font-size: 21.5px;
    line-height: 28.5px;
  }
  .intro-question {
    position: absolute;
    left: 39px; top: 210px;
    color: var(--navy);
    font-weight: 700;
    font-size: 21.5px;
  }
  .intro-body {
    position: absolute;
    left: 38px; top: 275px; width: 330px;
    color: var(--navy);
    font-size: 15px;
    line-height: 21.3px;
    text-align: justify;
    hyphens: auto;
  }
  .intro-body p + p { margin-top: 21px; }
  .photo-relax {
    position: absolute;
    left: 0; top: 633px; width: 405px; height: 301px;
    background: linear-gradient(180deg, var(--garden-sky) 0%, var(--garden-green) 45%, var(--garden-deep) 100%);
  }
  .photo-relax__caption {
    position: absolute;
    left: 0; right: 0; top: 18px;
    text-align: center;
    color: var(--white);
    font-weight: 700;
    font-size: 17px;
    text-shadow: 0 1px 3px rgba(0,0,0,.75);
  }
  .contact-band {
    position: absolute;
    left: 0; top: 954px; width: 405px; height: 189px;
    background: var(--navy);
  }
  .contact-band__label {
    position: absolute;
    left: 74px; top: 80px;
    color: var(--white);
    font-family: "PT Serif", serif;
    font-size: 14px;
  }

  /* Voices panel */
  .photo-gardener {
    position: absolute;
    left: 0; top: 25px; width: 405px; height: 282px;
    background: linear-gradient(135deg, var(--garden-deep) 0%, var(--rose-green) 55%, #c9c4a8 100%);
  }
  .photo-couple {
    position: absolute;
    left: 0; top: 597px; width: 405px; height: 250px;
    background: linear-gradient(90deg, var(--room-mauve) 0%, #b49aa4 45%, var(--room-light) 100%);
  }
  .voice {
    position: absolute;
    left: 0; width: 405px;
    color: var(--white);
  }
  .voice--green { top: 306px; height: 263px; background: var(--green); }
  .voice--navy { top: 847px; height: 296px; background: var(--navy); }
  .voice__mark {
    position: absolute;
    font-weight: 700;
    font-style: italic;
    font-size: 62px;
    line-height: 1;
  }
  .voice__mark--open { left: 14px; top: 10px; }
  .voice--navy .voice__mark--open { left: 18px; top: 12px; }
  .voice__mark--close { right: 16px; }
  .voice--green .voice__mark--close { top: 168px; }
  .voice--navy .voice__mark--close { top: 232px; }
  .voice__quote {
    position: absolute;
    left: 51px; top: 26px; width: 330px;
    font-size: 15.3px;
    line-height: 21.4px;
  }
  .voice--navy .voice__quote { left: 22px; top: 32px; width: 355px; padding-left: 28px; text-align: justify; hyphens: auto; }
  .voice__question {
    position: absolute;
    left: 34px;
    font-size: 22.5px;
    line-height: 29px;
  }
  .voice--green .voice__question { top: 177px; }
  .voice--navy .voice__question { left: 38px; top: 190px; }
</style>
</head>
<body>

<section class="panel panel--intro">
  <h1 class="intro-headline">Viele Senioren plagen im Alter Geldsorgen und Ängste was mit dem geschieht, was man sich sein Leben lang aufgebaut hat.</h1>
  <h2 class="intro-question">Gehören Sie auch dazu?</h2>
  <div class="intro-body" lang="de">
    <p>Die XY-Genossenschaft hat sich darauf spezialisiert, Senioren einen ruhigen Lebensabend zu ermöglichen, indem wir Ihre Immobilie ankaufen. Für Sie ändert sich weiter nichts, Sie bleiben wie bisher in Ihrem Haus oder Ihrer Eigentumswohnung mit dem Unterschied, dass die Kosten für Steuern und Instandhaltung zukünftig von der Genossenschaft und nicht mehr von Ihrer Rente bezahlt werden. Das bedeutet für Sie eine Entlastung für Kopf und Geldbeutel.</p>
    <p>Rufen Sie uns unverbindlich an und informieren Sie sich über die Vorteile einer Mitgliedschaft in der XY-Genossenschaft.</p>
  </div>
  <div class="photo-relax" role="img" aria-label="Foto: Mann mit Strohhut entspannt im Liegestuhl in einem blühenden Garten">
    <p class="photo-relax__caption">Lehnen Sie sich entspannt zurück!</p>
  </div>
  <footer class="contact-band">
    <p class="contact-band__label">Kontaktdaten</p>
  </footer>
</section>

<section class="panel panel--voices">
  <div class="photo-gardener" role="img" aria-label="Foto: ältere Frau mit Sonnenhut pflegt Rosen im Garten"></div>
  <blockquote class="voice voice--green">
    <span class="voice__mark voice__mark--open">"</span>
    <p class="voice__quote">Ich bin noch fit genut, um meinen Garten und meinen Haushalt in Schuss zu halten - ich möchte hier nicht ausziehen.<br>Aber seit mein Mann vor zwei Jahren verstorben ist, muss ich mit meiner kleinen Rente und der Witwenrente jeden Cent umdrehen.</p>
    <p class="voice__question">Wie kann ich meine<br>Unterhaltungskosten senken?</p>
    <span class="voice__mark voice__mark--close">"</span>
  </blockquote>
  <div class="photo-couple" role="img" aria-label="Foto: älteres Ehepaar blickt nachdenklich aus dem Fenster"></div>
  <blockquote class="voice voice--navy">
    <span class="voice__mark voice__mark--open">"</span>
    <p class="voice__quote" lang="de">Meine Frau und ich haben unseren Sohn in dieser Wohnung groß gezogen. Bei einem Autounfall kam er vor fünf Jahren ums Leben. Nun wissen wir nicht, was mit unserer Wohnung passieren soll, wenn wir nicht mehr sind. Es gibt keine nahen Angehörigen mehr. Soll jemand fremdes alles erben?</p>
    <p class="voice__question">Wie können wir für den Erbfall<br>vorsorgen?</p>
    <span class="voice__mark voice__mark--close">"</span>
  </blockquote>
</section>

</body>
</html>
```